We are starting a new service that will combine local city menus and specials from local restaurants that will then be emailed and printed out on our website.. its a free service to the subscribers and a small charge to the restaurants. We need something to reflect the restaurant industry and to appeal to the general public alike, free to the end user. They sign up and receive daily specials in an email from our site.. not just one city but any one they pick that we service.. We would need links to include. Home, About Us, Sign Up (for free to public), Add Your Restaurant (increase sales and reduce daily calls).. and Contact Us link.. the name of the service is Town Plates in Motion and website will be townplatesinmotion.example. thank you

```html
<!DOCTYPE html>
<html lang="en">
<head>
<meta charset="utf-8">
<title>Town Plates in Motion</title>
<link rel="stylesheet" href="https://fonts.googleapis.com/css2?family=Didact+Gothic&display=swap">
<style>
:root{
  --ink:#222;
  --muted:#9a9a9a;
  --nav:#222;
  --nav-active:#0b0b0b;
  --link:#428bca;
  --accent:#5bc0de;
  --line:#e6e6e6;
  --field:#ccc;
  --white:#fff;
}
*{box-sizing:border-box;margin:0;padding:0}
html,body{width:1200px;height:1000px;overflow:hidden;background:var(--white)}
body{position:relative;font-family:"Didact Gothic",Verdana,sans-serif;color:var(--ink)}
.abs{position:absolute}
.brand-mark{left:14px;top:8px;display:flex;align-items:center;gap:6px;font-size:11px;color:var(--ink)}
.brand-mark i{display:block;width:14px;height:14px;background:#c0392b}
.navbar{left:0;top:44px;width:1182px;height:30px;background:var(--nav);border-bottom:1px solid #080808}
.nav-brand{left:40px;top:6px;font-size:14px;color:var(--muted);letter-spacing:.5px}
.nav-item{top:0;height:30px;line-height:30px;font-size:11px;color:#777;letter-spacing:.5px}
.nav-item.active{background:var(--nav-active);color:var(--white);font-weight:bold;text-align:center}
.caret{display:inline-block;border-left:4px solid transparent;border-right:4px solid transparent;border-top:4px solid #777;margin-left:4px;vertical-align:middle}
.search{left:787px;top:5px;width:262px;height:19px;background:var(--white);border-radius:3px;font-size:11px;color:#777;padding:2px 14px}
.btn{background:var(--white);border:1px solid var(--field);border-radius:3px;font-size:11px;text-align:center;color:var(--ink);letter-spacing:.8px}
.hero{left:40px;top:86px;width:1101px;height:203px;background:linear-gradient(110deg,#c8623a 0%,#8a3f26 12%,#2b2624 30%,#1a1918 60%,#2a2522 90%,#611a16 97%,#8b1d1a 100%)}
.hero-arrow{top:92px}
.dots{left:525px;top:175px;display:flex;gap:6px}
.dots span{width:9px;height:9px;border:1px solid var(--white);border-radius:50%}
.dots span.on{width:12px;height:12px;margin-top:-1px;background:var(--white)}
.signup-title{left:40px;top:333px;width:248px;text-align:center;font-size:18px;line-height:16px;letter-spacing:1px}
.small-copy{font-size:10.5px;line-height:9.9px;text-align:justify;letter-spacing:1.2px}
.field{border:1px solid var(--field);border-radius:3px;font-size:11px;color:#777;padding:2px 14px;height:20px;letter-spacing:.8px}
.btn-primary{background:var(--accent);color:var(--white);border-radius:2px;text-align:center;font-size:11px;letter-spacing:.8px;height:19px;line-height:19px}
.terms{left:40px;top:562px;width:268px;text-align:center;font-size:10.5px;line-height:10px;letter-spacing:1px}
.terms a,.link{color:var(--link);text-decoration:none}
.photo{top:324px;width:176px;height:135px}
.card-title{top:463px;width:246px;text-align:center;font-size:10px;color:var(--link);letter-spacing:.8px}
.read{top:593px;width:115px;height:21px;line-height:19px}
.rule{left:48px;width:1104px;height:1px;background:var(--line)}
.section-title{left:0;width:1200px;top:673px;text-align:center;font-size:16px;color:var(--link);letter-spacing:1px}
.perk{left:138px;width:444px}
.perk h3{font-weight:normal;font-size:15px;color:var(--link);letter-spacing:1px;line-height:17px}
.perk p{font-size:14px;line-height:12.5px;text-align:justify;letter-spacing:1.5px}
.wide-field{left:618px;width:444px}
.foot-col{top:905px;font-size:10.5px;letter-spacing:.8px}
.foot-col h4{font-weight:normal;text-transform:uppercase;font-size:10.5px;margin-bottom:3px}
.foot-col ul{list-style:square;padding-left:46px;line-height:10.5px}
.foot-col ul.social{list-style:none;padding-left:0}
.social li{display:flex;align-items:center;gap:2px;height:18.5px}
.social li::before{content:"";width:4px;height:4px;background:var(--ink);border-radius:50%;margin-right:10px}
.social i{display:block;width:20px;height:18px;border-radius:50%;background:var(--ink)}
.copyright{left:0;width:1200px;top:982px;text-align:center;font-size:10.5px;letter-spacing:.8px}
</style>
</head>
<body>
  <div class="abs brand-mark"><i></i>Town Plates in Motion</div>

  <nav class="abs navbar">
    <div class="abs nav-brand">TOWN PLATES in MOTION</div>
    <div class="abs nav-item active" style="left:456px;width:78px">Home</div>
    <div class="abs nav-item" style="left:552px">About Us<span class="caret"></span></div>
    <div class="abs nav-item" style="left:671px">Contact Us</div>
    <div class="abs search">Search</div>
    <div class="abs btn" style="left:1055px;top:5px;width:84px;height:19px;line-height:17px">Submit</div>
  </nav>

  <div class="abs hero" role="img" aria-label="Close-up of a restaurant menu cover on a table">
    <svg class="abs hero-arrow" style="left:72px" width="24" height="18" viewBox="0 0 24 18"><path d="M14 0 L0 9 L14 18 L10 9 Z" fill="#ddd"/></svg>
    <svg class="abs hero-arrow" style="left:1008px" width="24" height="18" viewBox="0 0 24 18"><path d="M10 0 L24 9 L10 18 L14 9 Z" fill="#ddd"/></svg>
    <div class="abs dots"><span></span><span class="on"></span><span></span></div>
  </div>

  <h2 class="abs signup-title" style="font-weight:normal">Sign Up with TOWN<br>PLATES</h2>
  <p class="abs small-copy" style="left:40px;top:372px;width:248px">Lorem Ipsum is simply dummy text of the printing and typesetting industry. Lorem Ipsum has been the industry's standard dummy text ever since the 1500s, when an unknown printer took a galley of type and scrambled it to make a type specimen book.</p>
  <div class="abs field" style="left:49px;top:458px;width:250px">Your E-mail</div>
  <div class="abs field" style="left:49px;top:486px;width:250px">Password</div>
  <div class="abs field" style="left:49px;top:506px;width:250px">Confirmation</div>
  <div class="abs btn-primary" style="left:49px;top:534px;width:250px">Sign Up</div>
  <p class="abs terms">By signing up you agree to <a href="#">Terms of Use</a> and <a href="#">Privacy Policy</a></p>

  <div class="abs photo" style="left:360px;background:linear-gradient(135deg,#7a3b1c,#c47a3a 50%,#e9d9c2)" role="img" aria-label="Grilled chicken plate with vegetables"></div>
  <div class="abs card-title" style="left:335px">DAILY SPECIAL</div>
  <p class="abs small-copy" style="left:335px;top:479px;width:246px">Lorem Ipsum is simply dummy text of the printing and typesetting industry. Lorem Ipsum has been the industry's standard dummy text ever since the 1500s, when an unknown printer took a galley of type and scrambled it to make a type specimen book. It has survived not only five centuries, but also the leap into electronic typesetting, remaining essentially unchanged.</p>
  <div class="abs btn read" style="left:401px">Read More</div>

  <div class="abs photo" style="left:645px;background:linear-gradient(180deg,#3a3a3a 0%,#f4f4f4 25%,#fafafa 100%)" role="img" aria-label="Printed restaurant menu card"></div>
  <div class="abs card-title" style="left:619px">MENU COMBO</div>
  <p class="abs small-copy" style="left:619px;top:479px;width:246px">Lorem Ipsum is simply dummy text of the printing and typesetting industry. Lorem Ipsum has been the industry's standard dummy text ever since the 1500s, when an unknown printer took a galley of type and scrambled it to make a type specimen book. It has survived not only five centuries, but also the leap into electronic typesetting, remaining essentially unchanged.</p>
  <div class="abs btn read" style="left:685px">Read More</div>

  <div class="abs photo" style="left:928px;background:linear-gradient(180deg,#1d3556 0%,#c7653a 35%,#2a2430 60%,#0e0f1a 100%)" role="img" aria-label="City skyline at dusk"></div>
  <div class="abs card-title" style="left:903px">LOCATE A RESTAURANT</div>
  <p class="abs small-copy" style="left:903px;top:479px;width:246px">Lorem Ipsum is simply dummy text of the printing and typesetting industry. Lorem Ipsum has been the industry's standard dummy text ever since the 1500s, when an unknown printer took a galley of type and scrambled it to make a type specimen book. It has survived not only five centuries, but also the leap into electronic typesetting, remaining essentially unchanged.</p>
  <div class="abs btn read" style="left:969px">Read More</div>

  <div class="abs rule" style="top:625px"></div>

  <h2 class="abs section-title" style="font-weight:normal">Add You Restaurant</h2>
  <div class="abs perk" style="top:698px">
    <h3>Increase Sales</h3>
    <p>Lorem Ipsum has been the industry's standard dummy text ever since the 1500s, when an unknown printer took a galley of type and scrambled it to make a type specimen book.</p>
  </div>
  <div class="abs perk" style="top:773px">
    <h3>Reduce Daily Calls</h3>
    <p>Lorem Ipsum has been the industry's standard dummy text ever since the 1500s, when an unknown printer took a galley of type and scrambled it to make a type specimen book.</p>
  </div>
  <div class="abs field wide-field" style="top:696px">Restaurant Name</div>
  <div class="abs field wide-field" style="top:724px">Location</div>
  <div class="abs field wide-field" style="top:753px">Lorem Ipsum</div>
  <div class="abs field wide-field" style="top:781px">Lorem Ipsum</div>
  <div class="abs btn-primary wide-field" style="top:810px;font-weight:bold">Submit</div>

  <div class="abs rule" style="top:890px"></div>

  <div class="abs foot-col" style="left:67px">
    <h4>Find a Restaurant</h4>
    <ul><li>Europe</li><li>N. America</li><li>Asia</li><li>Australia</li><li>S. America</li></ul>
  </div>
  <div class="abs foot-col" style="left:342px">
    <h4>About Us</h4>
    <ul><li>Our Blog</li><li>Recipes</li><li>Plates in Motion</li></ul>
  </div>
  <div class="abs foot-col" style="left:618px">
    <h4>All Menus</h4>
    <ul><li>Today's Specials</li><li>Lorem Ipsum</li></ul>
  </div>
  <div class="abs foot-col" style="left:893px">
    <h4>Connect with Us</h4>
    <ul class="social">
      <li><i></i><a class="link" href="#">Friendbook</a></li>
      <li><i></i><a class="link" href="#">Talk</a></li>
      <li><i></i><a class="link" href="#">Chirper</a></li>
    </ul>
  </div>

  <p class="abs copyright">Copyright © Town Plates in Motion 2014</p>
</body>
</html>
```